Brindo like IOS/Android app for Okinawa Island - LumaTrail

LumaTrail is the name of the app
The closest thing that I can relate this app to is a region specific Brindo app. The app is for the island of Okinawa and is geared towards English speaking travelers. The style of app that I prefer is a look and feel similar to that of the new Nestora app, color should also be similar if not the same as the nestora app.

The app needs to have the following screens

LOGIN SCREEN
1. App login page with a login for chatterly button or create an account option. Personally I would like an image in the background with a real beachy feel, but don't do this if it messes with your design.

2. Depending on the choice of login there will need to be a second login screen to create the account. Nestora does this nicely.

PRIMARY HOME
primary page similar to the primary layout when you get into the nestora app.
This page is kind of like the home page of the app and should include the following items:
search field
upcoming events
popular things to do
featured restaurants
Featured Places to stay
area guides
Moving here
(this will allow the person to select, housing agencies, auto dealers, schools etc) These are essentially just quick searches.
Each selection should be listed so that the user can swipe to the left or right in order to view more listings under the categories listed above. It will not be the full list but rather a sample.

SIDEBAR POPOUT MENU
Popout sidebar that contains the following selections
Places to Eat
Things to do
Attractions
Beaches
Shop
Farmers Markets
Places to Stay
Schools & DayCare
Housing
Auto
Events
Account settings
Add a business

LIST VIEW
4. List view page for whatever category the user selected. This will show all the listings for the specific category: The top should also have the featured listings for that category

INDIVIDUAL LISTING
5. Listing page
This will include photos, description, hours, map(this can be a button to view the map or the map), Reviews with a leave a review option

AREA GUIDES
6. Area Guides. This is where the user will be able to select a specific area and learn about it. It should include an area where there can be a description, photos with a hero photo image, a map, popular local attractions or things to do, best restaurants in the area, places to stay etc.

PROFILE PAGE
7. Profile page for the user where they can make any updates they need to

Every page but the listing page should include the search bar. When the user clicks in it they should be able to see a drop down of quick select searches or run a regular search.

Logo
I have attached a logo that was made that needs a redesign. The map marker contains the logo for Okinawa within it so it does need to be similar.

If you have any questions or need clarification please send me a message. I will respond promptly.
Thank you,

```html
<!DOCTYPE html>
<html lang="en">
<head>
<meta charset="utf-8">
<title>LumaTrail – Welcome</title>
<link rel="stylesheet" href="https://fonts.googleapis.com/css2?family=Josefin+Sans:wght@300;400;600&family=Inter:wght@400;600&display=swap">
<style>
  :root {
    --sky: #3c5876;
    --hill: #4b5a3a;
    --foliage: #3f6d37;
    --sand: #eceee8;
    --lagoon-light: #35d6d3;
    --lagoon: #1cb6b4;
    --lagoon-deep: #1a7b70;
    --white: #ffffff;
    --brand-coral: #e35a69;
    --social-blue: #3d5a98;
    --email-bg: #ffffff;
    --email-text: #707070;
    --email-icon: #6b6b6b;
  }
  * { box-sizing: border-box; margin: 0; padding: 0; }
  html, body { width: 676px; height: 1200px; overflow: hidden; background: var(--white); }
  .screen {
    position: relative;
    width: 676px;
    height: 1200px;
    overflow: hidden;
    font-family: "Josefin Sans", sans-serif;
  }
  .hero-photo {
    position: absolute;
    inset: 0 0 200px 0;
    background: linear-gradient(180deg,
      var(--sky) 0%,
      var(--sky) 9%,
      var(--hill) 14%,
      var(--foliage) 25%,
      var(--sand) 31%,
      var(--sand) 34%,
      var(--lagoon-light) 39%,
      var(--lagoon) 60%,
      var(--lagoon-deep) 100%);
  }
  .status-bar {
    position: absolute;
    top: 0; left: 0; right: 0;
    height: 40px;
    display: flex;
    align-items: center;
    justify-content: space-between;
    padding: 0 12px 0 14px;
    color: var(--white);
    font-family: "Inter", sans-serif;
    font-size: 19px;
  }
  .status-bar .time { font-weight: 600; position: absolute; left: 50%; transform: translateX(-50%); }
  .status-left, .status-right { display: flex; align-items: center; gap: 6px; }
  .brand {
    position: absolute;
    top: 176px;
    left: 0; right: 0;
    display: flex;
    justify-content: center;
    align-items: center;
    gap: 14px;
  }
  .brand-dot {
    width: 54px; height: 54px;
    border-radius: 50%;
    background: var(--brand-coral);
  }
  .brand-name {
    color: var(--white);
    font-size: 58px;
    font-weight: 600;
    line-height: 1;
    padding-top: 8px;
  }
  .auth-button {
    position: absolute;
    left: 0; right: 0;
    height: 100px;
    display: flex;
    align-items: center;
    justify-content: center;
    font-size: 34px;
    font-weight: 300;
    text-decoration: none;
  }
  .auth-button .icon {
    position: absolute;
    left: 44px;
    top: 50%;
    transform: translateY(-50%);
  }
  .auth-button .label { padding-top: 6px; padding-left: 16px; }
  .auth-social { top: 1000px; background: var(--social-blue); color: var(--white); }
  .auth-social .icon { width: 22px; height: 22px; left: 52px; border-radius: 50%; background: var(--white); }
  .auth-email { top: 1100px; background: var(--email-bg); color: var(--email-text); }
</style>
</head>
<body>
<main class="screen">
  <div class="hero-photo" role="img" aria-label="Photo of a white sand beach with thatched umbrellas, green hills and a turquoise lagoon beside rocky cliffs"></div>

  <div class="status-bar">
    <div class="status-left">
      <svg width="78" height="12" viewBox="0 0 78 12" aria-hidden="true">
        <g fill="#ffffff">
          <circle cx="6" cy="6" r="5"/><circle cx="19" cy="6" r="5"/><circle cx="32" cy="6" r="5"/><circle cx="45" cy="6" r="5"/><circle cx="58" cy="6" r="5"/>
        </g>
      </svg>
      <svg width="20" height="15" viewBox="0 0 20 15" aria-hidden="true">
        <path d="M10 14 L6.5 10.2 A5 5 0 0 1 13.5 10.2 Z" fill="#ffffff"/>
        <path d="M3.8 7.4 A9 9 0 0 1 16.2 7.4" stroke="#ffffff" stroke-width="2.2" fill="none"/>
        <path d="M1 4.4 A13 13 0 0 1 19 4.4" stroke="#ffffff" stroke-width="2.2" fill="none"/>
      </svg>
    </div>
    <span class="time">9:41 AM</span>
    <div class="status-right">
      <span>100%</span>
      <svg width="46" height="20" viewBox="0 0 46 20" aria-hidden="true">
        <rect x="1" y="1" width="40" height="18" rx="3" fill="none" stroke="#ffffff" stroke-width="1.6"/>
        <rect x="3.5" y="3.5" width="35" height="13" rx="1.5" fill="#ffffff"/>
        <rect x="42.5" y="7" width="2.5" height="6" rx="1" fill="#ffffff"/>
      </svg>
    </div>
  </div>

  <div class="brand">
    <span class="brand-dot" aria-hidden="true"></span>
    <span class="brand-name">LumaTrail</span>
  </div>

  <a class="auth-button auth-social" href="#">
    <span class="icon" aria-hidden="true"></span>
    <span class="label">Login with Chatterly</span>
  </a>

  <a class="auth-button auth-email" href="#">
    <svg class="icon" width="37" height="26" viewBox="0 0 37 26" aria-hidden="true">
      <path d="M0 0 H37 V2 L18.5 14 L0 2 Z" fill="var(--email-icon)"/>
      <path d="M0 6 L18.5 18 L37 6 V26 H0 Z" fill="var(--email-icon)"/>
    </svg>
    <span class="label">Sign in with Email</span>
  </a>
</main>
</body>
</html>
```